Business cards and stationary for a health and wellbeing company
Lumen Forms
Business cards and stationary for a health and wellbeing company - Health
Creative Brief
Bright & Fun-filled
Jolene prescott
Director
PO Box
sales@lumenforms.com.au
www.lumenforms.com.au
Hi, I am happy to have a wide selection of fonts and designs. Lumen Forms is a health conscious Australian business that sells protein, supplements, health equipment, meditation and beauty products. We pride ourselves on great customer service, great products and a true passion for feeling and looking good. Our target market is females aged 18-60 years of age, mums and woman who want to feel amazing. Colour • Pink • White • Blue • Purple
Im open to different designs.
JolenePrescott JolenePrescott
Hi Everyone, Thank you so much for your great designs! I love the bright colours and lines that flow rather than straight and sharp. Could you please show me the front as well as the back of the business cards. I am wanting to change the font on my logo? I am wanting it so that the word Lumen sits above the word forms. Looking forward to some great designs! Thanks!

```html
<!DOCTYPE html>
<html lang="en">
<head>
<meta charset="utf-8">
<title>Lumen Forms Stationery</title>
<link rel="stylesheet" href="https://fonts.googleapis.com/css2?family=Nunito:wght@400;600;800&display=swap">
<style>
  :root {
    --magenta: #c02fbb;
    --magenta-deep: #8f1f8c;
    --magenta-light: #e05fdb;
    --cyan: #2bb5e6;
    --brand: #9a2a97;
    --paper: #ffffff;
    --stage: #eceef0;
    --ink: #555a60;
    --ink-soft: #8a8f95;
  }
  * { box-sizing: border-box; margin: 0; padding: 0; }
  html, body { width: 1200px; height: 936px; overflow: hidden; }
  body { background: var(--stage); font-family: "Nunito", sans-serif; color: var(--ink); position: relative; }

  .sheet { position: absolute; background: var(--paper); box-shadow: 0 3px 10px rgba(0,0,0,.18); overflow: hidden; }
  .wave { position: absolute; inset: 0; width: 100%; height: 100%; }

  .brand { display: flex; align-items: center; gap: 8px; position: absolute; }
  .brand-dot { border-radius: 50%; background: var(--cyan); flex: none; }
  .brand-name { font-weight: 800; color: var(--brand); white-space: nowrap; letter-spacing: -.5px; }

  /* Letterhead */
  .letterhead { left: 20px; top: 25px; width: 583px; height: 584px; }
  .letterhead .brand { left: 36px; top: 44px; }
  .letterhead .brand-dot { width: 26px; height: 26px; }
  .letterhead .brand-name { font-size: 26px; }
  .letter { position: absolute; left: 40px; top: 120px; width: 440px; font-size: 7px; line-height: 1.55; color: var(--ink-soft); }
  .letter p { margin-bottom: 9px; }
  .letter .signature { width: 46px; height: 16px; margin: 4px 0 6px; }
  .letter .signer { color: var(--ink); font-weight: 600; }
  .letter-contact { position: absolute; left: 150px; top: 500px; font-size: 6.5px; line-height: 1.6; color: var(--ink-soft); }

  /* Folder */
  .folder { left: 634px; top: 25px; width: 538px; height: 591px; }
  .folder .brand { left: 0; right: 60px; top: 210px; flex-direction: column; gap: 14px; }
  .folder .brand-dot { width: 90px; height: 90px; }
  .folder .brand-name { font-size: 46px; }

  /* Business cards */
  .card-back { left: 46px; top: 647px; width: 203px; height: 114px; }
  .card-back .holder { position: absolute; left: 8px; top: 10px; color: #fff; font-size: 7px; line-height: 1.5; }
  .card-back .holder strong { font-size: 8px; display: block; }
  .card-back .details { position: absolute; left: 8px; top: 62px; color: var(--ink-soft); font-size: 5.5px; line-height: 1.55; }
  .card-back .brand { right: 10px; top: 14px; flex-direction: column; gap: 2px; }
  .card-back .brand-dot { width: 14px; height: 14px; }
  .card-back .brand-name { font-size: 9px; }

  .card-front { left: 46px; top: 781px; width: 203px; height: 120px; }
  .card-front .brand { left: 14px; top: 30px; flex-direction: column; gap: 6px; align-items: center; }
  .card-front .brand-dot { width: 26px; height: 26px; }
  .card-front .brand-name { font-size: 19px; }

  /* Envelopes */
  .envelope-front { left: 266px; top: 665px; width: 579px; height: 236px; }
  .envelope-front .brand { left: 26px; top: 34px; }
  .envelope-front .brand-dot { width: 24px; height: 24px; }
  .envelope-front .brand-name { font-size: 24px; }

  .envelope-back { left: 875px; top: 665px; width: 297px; height: 236px; }
  .envelope-back .web { position: absolute; left: 0; right: 0; top: 22px; text-align: center; color: #fff; font-size: 11px; letter-spacing: 2px; }
</style>
</head>
<body>

<section class="sheet letterhead" aria-label="Letterhead">
  <svg class="wave" viewBox="0 0 583 584" preserveAspectRatio="none" aria-hidden="true">
    <defs>
      <linearGradient id="lh-band" x1="0" y1="0" x2="0" y2="1">
        <stop offset="0" stop-color="var(--magenta-light)"/>
        <stop offset="1" stop-color="var(--magenta-deep)"/>
      </linearGradient>
    </defs>
    <path d="M528 0 C590 160 478 360 548 584 L583 584 L583 0 Z" fill="url(#lh-band)"/>
    <path d="M516 0 C578 160 466 360 536 584" fill="none" stroke="var(--cyan)" stroke-width="3"/>
  </svg>
  <div class="brand"><span class="brand-dot"></span><span class="brand-name">Lumen Forms</span></div>
  <div class="letter">
    <p>May 8, 2015</p>
    <p><span class="signer">Dear Customer,</span><br>12 Park Lane, Pelham QLD 4000</p>
    <p>Thank you for choosing us for your wellness journey. We are delighted to welcome you and share our range of protein, supplements, equipment and beauty products. Our team is always here to help you feel and look your very best every day.</p>
    <p>Please find enclosed the details of your order along with a guide to our latest meditation sessions. Let us know if anything is missing.</p>
    <p>We pride ourselves on caring service and a true passion for healthy living. If you have any questions about your products or would like advice on a routine, simply reply to this letter or call us during business hours.</p>
    <p>Kind regards,</p>
    <svg class="signature" viewBox="0 0 46 16" aria-hidden="true"><path d="M2 12 C8 2 12 2 10 12 C14 6 18 4 20 10 C24 4 30 6 34 9 C38 7 42 8 44 6" fill="none" stroke="var(--ink)" stroke-width="1"/></svg>
    <p><span class="signer">Jolene prescott</span><br>Director</p>
  </div>
  <div class="letter-contact">
    PO Box 12<br>Pelham QLD 4000<br>T 07 5550 0123<br>sales@lumenforms.com.au<br>www.lumenforms.com.au
  </div>
</section>

<section class="sheet folder" aria-label="Presentation folder">
  <svg class="wave" viewBox="0 0 538 591" preserveAspectRatio="none" aria-hidden="true">
    <defs>
      <linearGradient id="fd-band" x1="0" y1="0" x2="0" y2="1">
        <stop offset="0" stop-color="var(--magenta-light)"/>
        <stop offset="1" stop-color="var(--magenta-deep)"/>
      </linearGradient>
    </defs>
    <path d="M430 0 C520 170 372 380 452 591 L538 591 L538 0 Z" fill="url(#fd-band)"/>
    <path d="M414 0 C504 170 356 380 436 591" fill="none" stroke="var(--cyan)" stroke-width="5"/>
  </svg>
  <div class="brand"><span class="brand-dot"></span><span class="brand-name">Lumen Forms</span></div>
</section>

<section class="sheet card-back" aria-label="Business card, contact side">
  <svg class="wave" viewBox="0 0 203 114" preserveAspectRatio="none" aria-hidden="true">
    <path d="M0 0 L132 0 C150 20 110 40 128 56 L0 56 Z" fill="var(--magenta)"/>
    <path d="M0 58 L126 58 C112 42 152 22 136 0" fill="none" stroke="var(--cyan)" stroke-width="1.5"/>
  </svg>
  <div class="holder"><strong>Jolene prescott</strong>Director</div>
  <div class="details">M 0400 555 012<br>sales@lumenforms.com.au<br>www.lumenforms.com.au</div>
  <div class="brand"><span class="brand-dot"></span><span class="brand-name">Lumen Forms</span></div>
</section>

<section class="sheet card-front" aria-label="Business card, brand side">
  <svg class="wave" viewBox="0 0 203 120" preserveAspectRatio="none" aria-hidden="true">
    <path d="M168 0 C196 40 150 80 180 120 L203 120 L203 0 Z" fill="var(--magenta)"/>
    <path d="M160 0 C188 40 142 80 172 120" fill="none" stroke="var(--cyan)" stroke-width="1.5"/>
  </svg>
  <div class="brand"><span class="brand-dot"></span><span class="brand-name">Lumen Forms</span></div>
</section>

<section class="sheet envelope-front" aria-label="Envelope, front">
  <svg class="wave" viewBox="0 0 579 236" preserveAspectRatio="none" aria-hidden="true">
    <path d="M520 0 C560 70 500 150 548 236 L579 236 L579 0 Z" fill="var(--magenta)"/>
    <path d="M508 0 C548 70 488 150 536 236" fill="none" stroke="var(--cyan)" stroke-width="3"/>
  </svg>
  <div class="brand"><span class="brand-dot"></span><span class="brand-name">Lumen Forms</span></div>
</section>

<section class="sheet envelope-back" aria-label="Envelope, back">
  <svg class="wave" viewBox="0 0 297 236" preserveAspectRatio="none" aria-hidden="true">
    <path d="M0 0 L297 0 L297 62 L148 112 L0 62 Z" fill="var(--magenta)"/>
    <path d="M0 66 L148 116 L297 66" fill="none" stroke="var(--cyan)" stroke-width="2"/>
  </svg>
  <div class="web">www.lumenforms.com.au</div>
</section>

</body>
</html>
```